Manufacturing company needs new business card.

I need a unique Business Card that will truly stand out. Nothing too busy. Simple is good, right? Not looking for a standard design either. No cookie cutter layout. I am just looking for something interesting and a bit different. Does't have to completely off the wall crazy, just not your run of the mill business card. Clean and modern with a touch of industrial.

Target Market(s)

Air conditioning industry, Architects, builders.

Industry/Entity Type

Business

Contact Information for Business Card

Details to be included on card are:

Peter Vance
Managing Director

T: 1300 847 519
M: 0428 593 174
W: www.brenvaleworks.com.au
E: peter.vance@brenvaleworks.com.au
A: 58 Harwick Lane, Sydney NSW 2000

Font styles to use
Sans Serif

Colors
0355a3
848484
fbfbfb

Requirements
Must have
• Card design must be landscape.

```html
<!DOCTYPE html>
<html lang="en">
<head>
<meta charset="UTF-8">
<title>Brenvale Works – Business Card</title>
<link href="https://fonts.googleapis.com/css2?family=Quicksand:wght@500;700&display=swap" rel="stylesheet">
<style>
  :root {
    --brand-blue: #0355a3;
    --brand-grey: #848484;
    --card-white: #fbfbfb;
    --ink: #4a4a4a;
    --backdrop: #e7e4e0;
  }
  * { margin: 0; padding: 0; box-sizing: border-box; }
  html, body {
    width: 1200px;
    height: 799px;
    overflow: hidden;
    background: var(--backdrop);
    font-family: "Quicksand", sans-serif;
  }
  .canvas { position: relative; width: 1200px; height: 799px; }
  .card {
    position: absolute;
    top: 283px;
    width: 445px;
    height: 248px;
    background: var(--card-white);
    box-shadow: 0 2px 6px rgba(0,0,0,0.18);
    overflow: hidden;
  }
  .card--front { left: 139px; }
  .card--back { left: 624px; }
  .card__shapes { position: absolute; inset: 0; }
  .shape-fill { fill: var(--brand-blue); }
  .shape-line { fill: none; stroke: var(--brand-blue); stroke-width: 4; }

  .wordmark {
    position: absolute;
    display: flex;
    align-items: center;
    color: var(--brand-blue);
    font-weight: 700;
    white-space: nowrap;
  }
  .wordmark__square { background: var(--brand-grey); }
  .card--front .wordmark { left: 51px; top: 101px; gap: 14px; font-size: 30px; }
  .card--front .wordmark__square { width: 40px; height: 40px; }
  .card--back .wordmark { left: 258px; top: 147px; gap: 8px; font-size: 16px; }
  .card--back .wordmark__square { width: 24px; height: 24px; }

  .contact-list { position: absolute; left: 36px; top: 52px; list-style: none; }
  .contact-row {
    display: flex;
    align-items: center;
    gap: 8px;
    margin-bottom: 11px;
    color: var(--ink);
    font-size: 10px;
    font-weight: 500;
    line-height: 1.2;
  }
  .contact-icon {
    flex: none;
    width: 22px;
    height: 22px;
    border-radius: 3px;
    background: var(--brand-blue);
    display: flex;
    align-items: center;
    justify-content: center;
  }
  .contact-icon svg { width: 13px; height: 13px; fill: #fff; }
  .contact-icon .icon-stroke { fill: none; stroke: #fff; stroke-width: 1.3; }
  .contact-name { font-weight: 700; font-size: 11px; letter-spacing: 0.5px; text-transform: uppercase; }
</style>
</head>
<body>
<main class="canvas">

  <section class="card card--front">
    <svg class="card__shapes" viewBox="0 0 377 210" width="445" height="248" aria-hidden="true">
      <ellipse class="shape-line" cx="305" cy="0" rx="110" ry="78"/>
      <ellipse class="shape-fill" cx="308" cy="-2" rx="96" ry="68"/>
      <ellipse class="shape-line" cx="175" cy="238" rx="108" ry="68"/>
    </svg>
    <div class="wordmark">
      <span class="wordmark__square"></span>
      <span class="wordmark__name">Brenvale Works</span>
    </div>
  </section>

  <section class="card card--back">
    <svg class="card__shapes" viewBox="0 0 377 210" width="445" height="248" aria-hidden="true">
      <ellipse class="shape-line" cx="305" cy="0" rx="110" ry="78"/>
      <ellipse class="shape-fill" cx="308" cy="-2" rx="96" ry="68"/>
      <ellipse class="shape-line" cx="175" cy="238" rx="108" ry="68"/>
    </svg>

    <ul class="contact-list">
      <li class="contact-row">
        <span class="contact-icon"><svg viewBox="0 0 16 16"><circle cx="8" cy="5" r="3.2"/><path d="M2 15c0-3.5 2.7-5.5 6-5.5s6 2 6 5.5z"/></svg></span>
        <span><span class="contact-name">Peter Vance</span><br>Managing Director</span>
      </li>
      <li class="contact-row">
        <span class="contact-icon"><svg viewBox="0 0 16 16"><path d="M1 6c0-2 3-3.5 7-3.5S15 4 15 6v1.5h-3.5V6h-7v1.5H1z"/><path d="M3 9h10l1 5H2z"/></svg></span>
        <span>1300 847 519<br>0428 593 174</span>
      </li>
      <li class="contact-row">
        <span class="contact-icon"><svg viewBox="0 0 16 16"><g class="icon-stroke"><circle cx="8" cy="8" r="6.3"/><ellipse cx="8" cy="8" rx="2.8" ry="6.3"/><path d="M1.7 8h12.6M2.8 4.8h10.4M2.8 11.2h10.4"/></g></svg></span>
        <span>www.brenvaleworks.com.au<br>peter.vance@brenvaleworks.com.au</span>
      </li>
      <li class="contact-row">
        <span class="contact-icon"><svg viewBox="0 0 16 16"><path d="M8 1.5 1 8h2v6.5h3.5v-4h3v4H13V8h2z"/></svg></span>
        <span>58 Harwick Lane,<br>Sydney NSW 2000</span>
      </li>
    </ul>

    <div class="wordmark">
      <span class="wordmark__square"></span>
      <span class="wordmark__name">Brenvale Works</span>
    </div>
  </section>

</main>
</body>
</html>
```